PWRPT design for Company

Project: Develop a pwrpt for KL7ux. This can be just a blank pwrpt with standard templates that we can use to build our content and solutions around.
Website: www.kl7ux.example
Color Pallet: Try to use the color schema from our website.
PWRPT Design Tips: While we are a research-based company, our primary target is schools and school districts. We say our work is RESEARCH, POLICY, AND PRACTICE. I would like images that represent “WHY” our research matters, i.e. students, teachers, and administrators. If you can use images and stock photos that represent students with diverse backgrounds, teachers that are diverse and clearly teaching, and administrators that run a school, university, etc. We are in the process of updating our website, but the color scheme will remain the same.
Additional Information:
We built, researched, and designed, www.pvra-tq.example .
We built, researched, and designed, http://87wkgamma.example/olav/index.html
Target Market(s)
EDUCATION
Industry/Entity Type
It Company
Look and feel

```html
<!DOCTYPE html>
<html lang="en">
<head>
<meta charset="utf-8">
<title>KL7ux Presentation Templates</title>
<link rel="stylesheet" href="https://fonts.googleapis.com/css2?family=Ubuntu:wght@300;400;500;700&family=Arimo:wght@400;700&display=swap">
<style>
  :root{
    --stage-a:#f77f22;
    --stage-b:#f26b12;
    --coral:#ef6a4f;
    --sun:#f8d94a;
    --slate:#4a5e5d;
    --ink:#333b3d;
    --paper:#ffffff;
    --photo-a:#8c8c8c;
    --photo-b:#3e3e3e;
  }
  *{margin:0;padding:0;box-sizing:border-box}
  html,body{width:1200px;height:900px;overflow:hidden}
  body{background:radial-gradient(circle at 50% 45%,var(--stage-a),var(--stage-b));position:relative;font-family:"Arimo",Arial,sans-serif}
  .slide{position:absolute;width:338px;height:261px;background:var(--paper);overflow:hidden}
  .slide svg{display:block;width:100%;height:100%}
  .slide-cover{left:78px;top:183px}
  .slide-about{left:426px;top:183px}
  .slide-timeline{left:773px;top:183px}
  .slide-chart{left:78px;top:471px}
  .slide-media{left:426px;top:471px}
  .slide-flow{left:773px;top:471px}
  .title{font-family:"Ubuntu",sans-serif;font-weight:300;font-size:18px;fill:var(--ink)}
  .brand{font-family:"Ubuntu",sans-serif;font-weight:300;font-size:22px;fill:var(--slate);text-transform:uppercase;letter-spacing:1px}
  .body{font-family:"Arimo",sans-serif;font-size:5.4px;fill:var(--ink)}
  .tiny{font-family:"Arimo",sans-serif;font-size:3.4px;fill:#555}
  .tiny-light{font-family:"Arimo",sans-serif;font-size:3.6px;fill:#fff}
  .item-title{font-family:"Arimo",sans-serif;font-weight:700;font-size:5.5px;fill:var(--ink)}
  .pg{font-family:"Arimo",sans-serif;font-size:7px;fill:#555}
  .step-letter{font-family:"Ubuntu",sans-serif;font-weight:700;font-size:14px;fill:var(--paper)}
  .step-num{font-family:"Ubuntu",sans-serif;font-weight:700;font-size:7px;fill:var(--paper)}
  .opt-num{font-family:"Ubuntu",sans-serif;font-weight:500;font-size:17px;fill:var(--paper)}
  .opt-sub{font-family:"Arimo",sans-serif;font-size:5px;fill:var(--paper)}
  .opt-label{font-family:"Ubuntu",sans-serif;font-weight:700;font-size:7.5px;fill:var(--ink)}
  .footer-note{font-family:"Arimo",sans-serif;font-size:6.5px;fill:var(--ink)}
</style>
</head>
<body>
<svg width="0" height="0" style="position:absolute" aria-hidden="true">
  <defs>
    <linearGradient id="facet" x1="0" y1="0" x2="1" y2="1">
      <stop offset="0" stop-color="#fde6ec"/>
      <stop offset=".45" stop-color="#f7a0b3"/>
      <stop offset=".75" stop-color="#f2667a"/>
      <stop offset="1" stop-color="#f8c74a"/>
    </linearGradient>
    <linearGradient id="ribbon" x1="0" x2="1">
      <stop offset="0" stop-color="#f68a78"/>
      <stop offset=".6" stop-color="#fbd1c6"/>
      <stop offset="1" stop-color="#fff" stop-opacity="0"/>
    </linearGradient>
    <linearGradient id="photo" x1="0" y1="0" x2="1" y2="1">
      <stop offset="0" stop-color="var(--photo-a)"/>
      <stop offset="1" stop-color="var(--photo-b)"/>
    </linearGradient>
  </defs>
</svg>

<!-- Cover -->
<div class="slide slide-cover">
  <svg viewBox="0 0 422 326">
    <rect x="35" y="22" width="22" height="22" fill="var(--coral)"/>
    <text class="brand" x="66" y="41">KL7ux</text>
    <rect x="284" y="66" width="138" height="11" fill="var(--coral)"/>
    <rect x="0" y="71" width="422" height="200" fill="url(#photo)" role="img" aria-label="Black and white photo of cheering students with their teacher in a classroom"/>
    <rect x="0" y="261" width="422" height="13" fill="var(--slate)"/>
    <rect x="284" y="256" width="138" height="12" fill="var(--coral)"/>
    <text class="footer-note" x="211" y="292" text-anchor="middle">© 2017 All rights reserved. Contains confidential and proprietary information and may not be disclosed or reproduced</text>
    <text class="footer-note" x="211" y="301" text-anchor="middle">without the prior written consent of KL7ux</text>
  </svg>
</div>

<!-- About -->
<div class="slide slide-about">
  <svg viewBox="0 0 422 326">
    <polygon points="330,0 422,0 422,326 380,326 355,200 395,120" fill="url(#facet)" opacity=".85" role="img" aria-label="Soft pink and yellow faceted background"/>
    <rect x="0" y="33" width="12" height="28" fill="var(--sun)"/>
    <rect x="12" y="33" width="250" height="28" fill="url(#ribbon)"/>
    <text class="title" x="30" y="54">About KL7ux, Llc.</text>
    <g class="body">
      <text x="30" y="74">KL7ux, LLC. has unique capabilities around the</text>
      <text x="30" y="81">research project management being proposed</text>
      <text x="30" y="88">by the pilot demonstration project for virtual</text>
      <text x="30" y="95">learning. The staff at KL7ux is comprised of</text>
      <text x="30" y="102">several aspects that range from policy, practice,</text>
      <text x="30" y="109">process, and technical. First, from the policy</text>
      <text x="30" y="116">standpoint, Dr. Varela has 25 years in public</text>
      <text x="30" y="123">education. Dr. Varela has worked in various</text>
      <text x="30" y="130">states to develop integrated virtual learning</text>
      <text x="30" y="137">programs, and has helped establish statewide</text>
      <text x="30" y="144">virtual systems focused on career and college</text>
      <text x="30" y="151">readiness in many regions. Policy work has</text>
      <text x="30" y="158">been directly related to career and college</text>
      <text x="30" y="165">readiness in K12 schools, with research</text>
      <text x="30" y="172">focused on individual career programs and</text>
      <text x="30" y="179">defining career and college readiness.</text>
      <text x="30" y="193">Additional staff includes Marten Oyelaran, an</text>
      <text x="30" y="200">economic and workplace specialist who directs</text>
      <text x="30" y="207">workforce programs for the Ostrava Trade</text>
      <text x="30" y="214">Council. He also regularly serves as a</text>

      <text x="180" y="74">subject matter expert in labor market analysis to</text>
      <text x="180" y="81">support career-driven curriculum development,</text>
      <text x="180" y="88">regional economic research and growth planning,</text>
      <text x="180" y="95">industry sector partnerships, educational</text>
      <text x="180" y="102">product development and public policy</text>
      <text x="180" y="109">recommendations. Personal experience in</text>
      <text x="180" y="116">secondary education, adult technical training</text>
      <text x="180" y="123">and workforce development have contributed to</text>
      <text x="180" y="130">a practical and digestible approach to</text>
      <text x="180" y="137">interpreting and applying labor market data.</text>
      <text x="180" y="144">An in-demand public speaker, he has addressed</text>
      <text x="180" y="151">a range of audiences both national and local,</text>
      <text x="180" y="158">including the Halvard Board Forum. Before</text>
      <text x="180" y="165">joining, he provided leadership to some of the</text>
      <text x="180" y="172">most innovative and successful career-driven</text>
      <text x="180" y="179">education and workforce development</text>
      <text x="180" y="186">initiatives, including the Norrland Career</text>
      <text x="180" y="193">Readiness Initiative. His writing and research</text>
      <text x="180" y="200">have contributed to successful efforts to</text>
      <text x="180" y="207">secure regional innovation and workforce</text>
      <text x="180" y="214">federal grants.</text>
    </g>
    <rect x="0" y="301" width="422" height="10" fill="var(--sun)"/>
    <rect x="18" y="298" width="22" height="16" fill="var(--paper)"/>
    <text class="pg" x="24" y="309">01</text>
    <rect x="284" y="293" width="138" height="12" fill="var(--coral)"/>
  </svg>
</div>

<!-- Timeline -->
<div class="slide slide-timeline">
  <svg viewBox="0 0 422 326">
    <polygon points="330,0 422,0 422,326 380,326 355,200 395,120" fill="url(#facet)" opacity=".85" role="img" aria-label="Soft pink and yellow faceted background"/>
    <rect x="0" y="33" width="12" height="28" fill="var(--sun)"/>
    <rect x="12" y="33" width="250" height="28" fill="url(#ribbon)"/>
    <text class="title" x="30" y="54">Lorem Ipsum Dolor sit amet</text>
    <g>
      <circle cx="22" cy="92" r="3" fill="var(--ink)"/><text class="item-title" x="29" y="94">Title One</text>
      <text class="tiny" x="29" y="102">Nam pretium turpis et</text><text class="tiny" x="29" y="106">arcu. Duis arcu tortor,</text><text class="tiny" x="29" y="110">suscipit eget, imperdiet</text>
      <circle cx="22" cy="127" r="3" fill="var(--ink)"/><text class="item-title" x="29" y="129">Title Two</text>
      <text class="tiny" x="29" y="137">Nam pretium turpis et</text><text class="tiny" x="29" y="141">arcu. Duis arcu tortor,</text><text class="tiny" x="29" y="145">suscipit eget, imperdiet</text>
      <circle cx="22" cy="162" r="3" fill="var(--ink)"/><text class="item-title" x="29" y="164">Title Three</text>
      <text class="tiny" x="29" y="172">Nam pretium turpis et</text><text class="tiny" x="29" y="176">arcu. Duis arcu tortor,</text><text class="tiny" x="29" y="180">suscipit eget, imperdiet</text>
      <circle cx="22" cy="197" r="3" fill="var(--ink)"/><text class="item-title" x="29" y="199">Title Four</text>
      <text class="tiny" x="29" y="207">Nam pretium turpis et</text><text class="tiny" x="29" y="211">arcu. Duis arcu tortor,</text><text class="tiny" x="29" y="215">suscipit eget, imperdiet</text>
      <circle cx="22" cy="233" r="3" fill="var(--ink)"/><text class="item-title" x="29" y="235">Title Five</text>
      <text class="tiny" x="29" y="243">Nam pretium turpis et</text><text class="tiny" x="29" y="247">arcu. Duis arcu tortor,</text><text class="tiny" x="29" y="251">suscipit eget, imperdiet</text>
    </g>
    <rect x="89" y="232" width="290" height="12" rx="2" fill="var(--sun)"/>
    <path d="M89 252 H379" stroke="var(--ink)" stroke-width="1.5" fill="none"/>
    <g fill="var(--ink)">
      <polygon points="89,210 95,216 89,222"/><polygon points="146,210 152,216 146,222"/>
      <polygon points="205,210 211,216 205,222"/><polygon points="262,210 268,216 262,222"/><polygon points="319,210 325,216 319,222"/>
    </g>
    <g>
      <rect x="108" y="173" width="6" height="65" fill="var(--sun)"/>
      <circle cx="111" cy="173" r="24" fill="var(--sun)"/><path d="M111 149 A24 24 0 0 1 111 197 Z" fill="var(--coral)"/>
      <text class="step-letter" x="95" y="178">A</text><circle cx="124" cy="173" r="4" fill="var(--paper)"/>
      <rect x="166" y="160" width="6" height="78" fill="var(--sun)"/>
      <circle cx="169" cy="160" r="24" fill="var(--sun)"/><path d="M169 136 A24 24 0 0 1 169 184 Z" fill="var(--coral)"/>
      <text class="step-letter" x="153" y="165">B</text><circle cx="181" cy="159" r="3.5" fill="none" stroke="#fff" stroke-width="1.5"/>
      <rect x="223" y="147" width="6" height="91" fill="var(--sun)"/>
      <circle cx="226" cy="147" r="24" fill="var(--sun)"/><path d="M226 123 A24 24 0 0 1 226 171 Z" fill="var(--coral)"/>
      <text class="step-letter" x="210" y="152">C</text><rect x="235" y="143" width="8" height="8" fill="var(--paper)"/>
      <rect x="281" y="133" width="6" height="105" fill="var(--sun)"/>
      <circle cx="284" cy="133" r="24" fill="var(--sun)"/><path d="M284 109 A24 24 0 0 1 284 157 Z" fill="var(--coral)"/>
      <text class="step-letter" x="268" y="138">D</text><path d="M297 127 V140 M293 130 H301" stroke="#fff" stroke-width="1.5"/>
      <rect x="338" y="120" width="6" height="118" fill="var(--sun)"/>
      <circle cx="341" cy="120" r="24" fill="var(--sun)"/><path d="M341 96 A24 24 0 0 1 341 144 Z" fill="var(--coral)"/>
      <text class="step-letter" x="325" y="125">E</text><path d="M351 126 L359 116" stroke="#fff" stroke-width="2"/>
    </g>
    <g>
      <circle cx="120" cy="238" r="8" fill="var(--ink)"/><text class="step-num" x="120" y="240.5" text-anchor="middle">01</text>
      <circle cx="177" cy="238" r="8" fill="var(--ink)"/><text class="step-num" x="177" y="240.5" text-anchor="middle">02</text>
      <circle cx="235" cy="238" r="8" fill="var(--ink)"/><text class="step-num" x="235" y="240.5" text-anchor="middle">03</text>
      <circle cx="292" cy="238" r="8" fill="var(--ink)"/><text class="step-num" x="292" y="240.5" text-anchor="middle">04</text>
      <circle cx="349" cy="238" r="8" fill="var(--ink)"/><text class="step-num" x="349" y="240.5" text-anchor="middle">05</text>
    </g>
    <rect x="0" y="301" width="422" height="10" fill="var(--sun)"/>
    <rect x="18" y="298" width="22" height="16" fill="var(--paper)"/>
    <text class="pg" x="24" y="309">02</text>
    <rect x="284" y="293" width="138" height="12" fill="var(--coral)"/>
  </svg>
</div>

<!-- Chart -->
<div class="slide slide-chart">
  <svg viewBox="0 0 422 326">
    <polygon points="330,0 422,0 422,326 380,326 355,200 395,120" fill="url(#facet)" opacity=".85" role="img" aria-label="Soft pink and yellow faceted background"/>
    <rect x="0" y="33" width="12" height="28" fill="var(--sun)"/>
    <rect x="12" y="33" width="250" height="28" fill="url(#ribbon)"/>
    <text class="title" x="30" y="54">Chart</text>
    <g>
      <rect x="68" y="111" width="52" height="122" fill="var(--slate)"/>
      <rect x="126" y="111" width="52" height="122" fill="var(--slate)"/>
      <rect x="185" y="111" width="52" height="122" fill="var(--slate)"/>
      <rect x="244" y="111" width="52" height="122" fill="var(--slate)"/>
      <rect x="302" y="111" width="52" height="122" fill="var(--slate)"/>
    </g>
    <g>
      <circle cx="94" cy="102" r="26" fill="var(--coral)"/><text class="opt-num" x="94" y="108" text-anchor="middle">01</text><text class="opt-sub" x="94" y="117" text-anchor="middle">option</text>
      <circle cx="152" cy="102" r="26" fill="var(--coral)"/><text class="opt-num" x="152" y="108" text-anchor="middle">02</text><text class="opt-sub" x="152" y="117" text-anchor="middle">option</text>
      <circle cx="211" cy="102" r="26" fill="var(--coral)"/><text class="opt-num" x="211" y="108" text-anchor="middle">03</text><text class="opt-sub" x="211" y="117" text-anchor="middle">option</text>
      <circle cx="270" cy="102" r="26" fill="var(--coral)"/><text class="opt-num" x="270" y="108" text-anchor="middle">04</text><text class="opt-sub" x="270" y="117" text-anchor="middle">option</text>
      <circle cx="328" cy="102" r="26" fill="var(--coral)"/><text class="opt-num" x="328" y="108" text-anchor="middle">05</text><text class="opt-sub" x="328" y="117" text-anchor="middle">option</text>
    </g>
    <g class="tiny-light" text-anchor="middle">
      <text x="94" y="147">Nam pretium</text><text x="94" y="152">turpis et arcu.</text><text x="94" y="157">Duis arcu tortor,</text><text x="94" y="162">suscipit eget,</text><text x="94" y="167">imperdiet nec,</text><text x="94" y="172">Sed aliquam</text>
      <text x="152" y="147">Nam pretium</text><text x="152" y="152">turpis et arcu.</text><text x="152" y="157">Duis arcu tortor,</text><text x="152" y="162">suscipit eget,</text><text x="152" y="167">imperdiet nec,</text><text x="152" y="172">Sed aliquam</text>
      <text x="211" y="147">Nam pretium</text><text x="211" y="152">turpis et arcu.</text><text x="211" y="157">Duis arcu tortor,</text><text x="211" y="162">suscipit eget,</text><text x="211" y="167">imperdiet nec,</text><text x="211" y="172">Sed aliquam</text>
      <text x="270" y="147">Nam pretium</text><text x="270" y="152">turpis et arcu.</text><text x="270" y="157">Duis arcu tortor,</text><text x="270" y="162">suscipit eget,</text><text x="270" y="167">imperdiet nec,</text><text x="270" y="172">Sed aliquam</text>
      <text x="328" y="147">Nam pretium</text><text x="328" y="152">turpis et arcu.</text><text x="328" y="157">Duis arcu tortor,</text><text x="328" y="162">suscipit eget,</text><text x="328" y="167">imperdiet nec,</text><text x="328" y="172">Sed aliquam</text>
    </g>
    <g fill="var(--paper)">
      <circle cx="94" cy="208" r="15"/><circle cx="152" cy="208" r="15"/><circle cx="211" cy="208" r="15"/><circle cx="270" cy="208" r="15"/><circle cx="328" cy="208" r="15"/>
    </g>
    <g fill="var(--slate)" stroke="var(--slate)">
      <rect x="87" y="201" width="14" height="3" rx="1.5"/><rect x="87" y="206" width="14" height="3" rx="1.5"/><rect x="87" y="211" width="14" height="3" rx="1.5"/>
      <circle cx="152" cy="205" r="5" stroke="none"/><rect x="150" y="210" width="4" height="4" stroke="none"/>
      <circle cx="211" cy="210" r="6" stroke="none"/><rect x="209" y="200" width="4" height="4" stroke="none"/>
      <path d="M270 201 V216 M265 205 H275 M264 211 Q270 218 276 211" fill="none" stroke-width="1.6"/>
      <path d="M326 200 H330 V206 L335 215 H321 L326 206 Z" fill="none" stroke-width="1.6"/>
    </g>
    <rect x="0" y="301" width="422" height="10" fill="var(--sun)"/>
    <rect x="18" y="298" width="22" height="16" fill="var(--paper)"/>
    <text class="pg" x="24" y="309">03</text>
    <rect x="284" y="293" width="138" height="12" fill="var(--coral)"/>
  </svg>
</div>

<!-- Media -->
<div class="slide slide-media">
  <svg viewBox="0 0 422 326">
    <polygon points="330,0 422,0 422,326 380,326 355,200 395,120" fill="url(#facet)" opacity=".85" role="img" aria-label="Soft pink and yellow faceted background"/>
    <rect x="0" y="33" width="12" height="28" fill="var(--sun)"/>
    <rect x="12" y="33" width="250" height="28" fill="url(#ribbon)"/>
    <text class="title" x="30" y="54">Lorem Ipsum Dolor sit amet</text>
    <rect x="19" y="71" width="161" height="101" fill="#231f20"/>
    <rect x="19" y="182" width="161" height="101" fill="#231f20"/>
    <g class="body">
      <text x="197" y="75">subject matter expert in labor market analysis to support</text>
      <text x="197" y="82">career-driven curriculum development, regional economic</text>
      <text x="197" y="89">research and growth planning, industry sector partner-</text>
      <text x="197" y="96">ships, educational product development and public policy</text>
      <text x="197" y="103">recommendations. Persona</text>
      <text x="197" y="186">subject matter expert in labor market analysis to support</text>
      <text x="197" y="193">career-driven curriculum development, regional economic</text>
      <text x="197" y="200">research and growth planning, industry sector partner-</text>
      <text x="197" y="207">ships, educational product development and public policy</text>
      <text x="197" y="214">recommendations. Persona</text>
    </g>
    <rect x="0" y="301" width="422" height="10" fill="var(--sun)"/>
    <rect x="18" y="298" width="22" height="16" fill="var(--paper)"/>
    <text class="pg" x="24" y="309">03</text>
    <rect x="284" y="293" width="138" height="12" fill="var(--coral)"/>
  </svg>
</div>

<!-- Flow -->
<div class="slide slide-flow">
  <svg viewBox="0 0 422 326">
    <polygon points="330,0 422,0 422,326 380,326 355,200 395,120" fill="url(#facet)" opacity=".85" role="img" aria-label="Soft pink and yellow faceted background"/>
    <rect x="0" y="33" width="12" height="28" fill="var(--sun)"/>
    <rect x="12" y="33" width="250" height="28" fill="url(#ribbon)"/>
    <text class="title" x="30" y="54">Lorem Ipsum Dolor sit amet</text>
    <g fill="none" stroke="var(--slate)" stroke-width="2">
      <path d="M82 132 V161 H325 V132 M163 132 V161 M244 132 V161"/>
      <path d="M122 194 V161 M203 194 V161 M283 194 V161"/>
    </g>
    <g fill="var(--paper)" stroke="var(--slate)" stroke-width="2">
      <circle cx="82" cy="110" r="22"/><circle cx="163" cy="110" r="22"/><circle cx="244" cy="110" r="22"/><circle cx="325" cy="110" r="22"/>
    </g>
    <g fill="none" stroke="var(--slate)" stroke-width="2">
      <path d="M82 100 V122 M75 104 H89 M73 115 Q82 126 91 115"/><circle cx="82" cy="98" r="2.5"/>
      <path d="M159 99 H167 M160 99 V107 L153 120 H173 L166 107 V99"/>
      <circle cx="244" cy="107" r="7"/><path d="M241 116 H247 M241 119 H247"/>
    </g>
    <circle cx="325" cy="113" r="10" fill="var(--slate)"/><rect x="321" y="99" width="8" height="5" fill="var(--slate)"/>
    <text x="325" y="117" font-family="Arimo,sans-serif" font-weight="700" font-size="11" fill="#fff" text-anchor="middle">$</text>
    <g fill="var(--coral)">
      <circle cx="122" cy="217" r="23"/><circle cx="203" cy="217" r="23"/><circle cx="283" cy="217" r="23"/>
    </g>
    <g fill="none" stroke="#fff" stroke-width="2">
      <circle cx="125" cy="213" r="7"/><path d="M120 218 L113 226"/>
      <ellipse cx="203" cy="208" rx="9" ry="3"/><path d="M194 208 V225 M212 208 V225 M194 213 Q203 217 212 213 M194 219 Q203 223 212 219 M194 225 Q203 229 212 225"/>
      <circle cx="283" cy="217" r="11"/><path d="M283 210 V217 L288 221"/>
    </g>
    <g fill="var(--sun)">
      <polygon points="118,104 126,110 118,116"/><polygon points="199,104 207,110 199,116"/><polygon points="280,104 288,110 280,116"/>
      <polygon points="158,211 166,217 158,223"/><polygon points="239,211 247,217 239,223"/>
    </g>
    <g class="opt-label" text-anchor="middle">
      <text x="123" y="152">Option 01</text><text x="203" y="152">Option 03</text><text x="284" y="152">Option 05</text>
      <text x="163" y="180">Option 02</text><text x="242" y="180">Option 04</text>
    </g>
    <rect x="0" y="301" width="422" height="10" fill="var(--sun)"/>
    <rect x="18" y="298" width="22" height="16" fill="var(--paper)"/>
    <text class="pg" x="24" y="309">03</text>
    <rect x="284" y="293" width="138" height="12" fill="var(--coral)"/>
  </svg>
</div>
</body>
</html>
```